New Zealand Export company needs business cards

We need new business cards to match our new logo for a company based in New Zealand who deal specifically with the Pacific Islands. We source, consolidate and ship products out of New Zealand to the Pacific Islands. Will attach our old ones and also new logo.
Would like the Islands we deal with and the areas of work we have access to, to be included on the business cards.

Contact Information for Business Card

T +64 9 571 3048
F +64 9 571 6285
12-18 Kowhai Lane, Drury, 2113
PO Box 814, Drury, Auckland 2247, New Zealand
www.falconfreight.example.nz
E sales@falconfreight.example.nz

Font styles to use
Sans Serif

Colors
85abd2
33a6d7
ffffff

Requirements
Must have
• A company of PWM

```html
<!DOCTYPE html>
<html lang="en">
<head>
<meta charset="utf-8">
<title>Falcon Freight business cards</title>
<link href="https://fonts.googleapis.com/css2?family=Arimo:wght@400;700&display=swap" rel="stylesheet">
<style>
  :root {
    --backdrop: #242424;
    --card: #ffffff;
    --card-back: #f7fafd;
    --navy: #0b57a8;
    --cyan: #16a6e2;
    --grey: #8a8a8a;
    --rule-grey: #9a9a9a;
    --photo-deep: #3fa9dc;
    --photo-mid: #a8d4ee;
  }
  * { margin: 0; padding: 0; box-sizing: border-box; }
  html, body { width: 976px; height: 1200px; overflow: hidden; }
  body {
    background: var(--backdrop);
    font-family: "Arimo", Arial, sans-serif;
    position: relative;
  }
  .card {
    position: absolute;
    left: 138px;
    width: 692px;
    height: 431px;
    border-radius: 22px;
    background: var(--card);
    overflow: hidden;
    box-shadow: 0 8px 18px rgba(0,0,0,0.45);
  }
  .card--front { top: 144px; }
  .card--back { top: 627px; background: var(--card-back); }

  .brand {
    position: absolute;
    left: 0; right: 0;
    top: 178px;
    text-align: center;
  }
  .brand__name {
    display: inline-flex;
    align-items: center;
    gap: 12px;
    font-size: 44px;
    font-weight: 700;
    letter-spacing: 2px;
    color: var(--navy);
    line-height: 1;
  }
  .brand__mark {
    width: 30px; height: 30px;
    background: var(--cyan);
  }
  .brand__tagline {
    margin-top: 18px;
    font-size: 16px;
    letter-spacing: 3px;
    color: var(--grey);
  }

  .photo {
    position: absolute;
    left: 0; top: 0; bottom: 0;
    width: 520px;
    background: linear-gradient(100deg, var(--photo-deep) 0%, var(--photo-mid) 45%, rgba(247,250,253,0) 100%);
  }

  .contact {
    position: absolute;
    left: 336px;
    width: 320px;
    top: 82px;
    text-align: center;
  }
  .contact__name {
    font-size: 45px;
    font-weight: 700;
    color: var(--navy);
    line-height: 1;
  }
  .contact__role {
    display: flex;
    align-items: center;
    gap: 6px;
    margin: 6px 10px 0;
    font-size: 17px;
    color: var(--cyan);
  }
  .contact__role::before, .contact__role::after {
    content: "";
    flex: 1;
    height: 1px;
    background: var(--cyan);
  }
  .contact__phones {
    margin-top: 22px;
    font-size: 17px;
    color: var(--grey);
    line-height: 24px;
  }
  .contact__phones small { font-size: 14px; }
  .contact__address {
    margin: 8px auto 0;
    width: 224px;
    padding: 5px 0 6px;
    border-top: 1px solid var(--cyan);
    border-bottom: 1px solid var(--rule-grey);
    font-size: 14px;
    line-height: 18.5px;
    color: var(--cyan);
    white-space: nowrap;
  }
  .contact__online {
    margin-top: 4px;
    font-size: 16px;
    color: var(--grey);
    line-height: 23px;
    letter-spacing: 0.3px;
  }
  .contact__online div {
    display: flex; align-items: center; justify-content: center; gap: 5px;
  }
  .icon { width: 16px; height: 16px; flex: none; }
</style>
</head>
<body>
  <section class="card card--front">
    <div class="brand">
      <div class="brand__name"><span class="brand__mark"></span>FALCON FREIGHT</div>
      <div class="brand__tagline">A COMPANY OF PWM</div>
    </div>
  </section>

  <section class="card card--back">
    <div class="photo" role="img" aria-label="Photo of a forested Pacific island in clear blue sea under a bright sky"></div>
    <div class="contact">
      <h1 class="contact__name">Tessa Hale</h1>
      <div class="contact__role">sales manager</div>
      <div class="contact__phones">
        <div><small>Tel :</small> +64 9 571 3048</div>
        <div><small>Fax :</small>+64 9 571 6285</div>
      </div>
      <div class="contact__address">
        12-18 Kowhai Lane, Drury, 2113<br>
        PO Box 814 , Drury,<br>
        Auckland 2247, New Zealand
      </div>
      <div class="contact__online">
        <div>
          <svg class="icon" viewBox="0 0 16 16" fill="none" stroke="#2aa6e0" stroke-width="1"><circle cx="8" cy="8" r="7"/><ellipse cx="8" cy="8" rx="3" ry="7"/><path d="M1 8h14M2.5 4.5h11M2.5 11.5h11"/></svg>
          www.falconfreight.example.nz
        </div>
        <div>
          <svg class="icon" viewBox="0 0 16 16"><rect x="1" y="3" width="14" height="10" rx="1.5" fill="#2aa6e0"/><path d="M1.5 4l6.5 5 6.5-5" fill="none" stroke="#fff" stroke-width="1.2"/></svg>
          sales@falconfreight.example.nz
        </div>
      </div>
    </div>
  </section>
</body>
</html>
```